Company Website for an IT business called "BRIGHT CORRIDOR"

Complete website creation with text and graphics.
We need :
- modern and creative design for our IT company
- Content management system to edit text later on
- Integrate third party content from partner company
- Contact form (transfer by email)
Updates

Designs look the same

Target Market(s)

Small and medium business
private customers

Industry/Entity Type

Information Technology

Coding

Coded - Design and coding required

Number of Pages Required

1 page

Font styles to use
Sans Serif

Requirements
Must have
• Contact form
Link to legal information
Link to data protection (GDPR)
Link to website owner declaration
Nice to have
• Fresh and creative graphics for IT business

```html
<!DOCTYPE html>
<html lang="en">
<head>
<meta charset="utf-8">
<title>Bright Corridor – IT Business Company</title>
<link href="https://fonts.googleapis.com/css2?family=Lato:ital,wght@0,400;0,700;0,900;1,400&display=swap" rel="stylesheet">
<style>
:root{
  --blue:#149bd8;
  --blue-soft:#d6ecf7;
  --ink:#1e1e1e;
  --text:#555;
  --light:#f5f5f5;
  --line:#bdbdbd;
  --footer:#262626;
  --white:#fff;
}
*{box-sizing:border-box;margin:0;padding:0}
html,body{width:1200px;height:4392px;overflow:hidden}
body{font-family:'Lato',sans-serif;color:var(--ink);background:var(--white)}
a{color:inherit;text-decoration:none}
section,header,footer{position:relative;width:1200px;overflow:hidden}
.abs{position:absolute}

/* header */
.site-header{height:111px}
.brand{left:111px;top:30px;display:flex;align-items:center;gap:12px;font-size:28px;font-weight:700;letter-spacing:2px;color:var(--ink)}
.brand-mark{width:18px;height:18px;background:var(--blue)}
.top-contact{right:111px;top:24px;font-size:16px;font-weight:700;display:flex;gap:10px;align-items:center}
.top-contact svg{vertical-align:-2px;margin-right:4px}
.main-nav{right:111px;top:70px;display:flex;gap:24px;font-size:17px;font-weight:700}
.main-nav .active{color:var(--blue)}

/* hero */
.hero{height:591px}
.hero-photo{inset:0;background:linear-gradient(100deg,#4c5a5e 0%,#7b8a88 35%,#b7b6aa 60%,#6f6a5c 85%,#3f4a3c 100%)}
.hero-title{left:111px;top:150px;font-size:62px;font-weight:900;color:var(--white)}
.hero-sub{left:111px;top:238px;font-size:24px;color:var(--white)}
.btn-outline{display:inline-flex;align-items:center;justify-content:center;border:2px solid currentColor;font-weight:700}
.hero-btn{left:111px;top:298px;width:204px;height:58px;color:var(--white);font-size:18px}
.hero-dots{left:111px;top:510px;display:flex;gap:5px}
.hero-dots span{width:12px;height:12px;border-radius:50%;border:2px solid var(--white)}
.hero-dots span:first-child{background:var(--white)}

/* welcome */
.welcome{height:534px}
.welcome h1{left:111px;top:80px;font-size:44px;font-weight:900;line-height:52px}
.welcome p{left:111px;top:200px;width:405px;font-size:16px;line-height:27px;color:var(--text)}
.welcome-btn{left:111px;top:391px;width:159px;height:54px;color:var(--ink);font-size:17px}
.welcome-photo{left:557px;top:75px;width:531px;height:357px;background:linear-gradient(135deg,#cfc9c0,#8a8f94 50%,#5f4b3a)}
.play{left:792px;top:228px;width:64px;height:64px;border-radius:50%;background:#1d1d1d;display:flex;align-items:center;justify-content:center}
.about-badge{left:486px;top:46px;width:104px;height:89px;background:var(--blue);color:var(--white);padding:10px 0 0 20px;font-weight:900;font-size:19px;line-height:21px}
.about-badge small{display:block;font-size:14px;font-weight:700;line-height:18px}

/* services */
.services{height:890px;background:var(--light)}
.section-title{left:0;width:1200px;text-align:center;font-size:42px;font-weight:900}
.services .section-title{top:52px}
.service{top:136px;width:200px;text-align:center}
.service-ring{width:184px;height:184px;margin:0 auto;border-radius:50%;border:2px solid var(--line);background:var(--white);display:flex;align-items:center;justify-content:center}
.service.current .service-ring{border-color:var(--blue)}
.service-icon{width:96px;height:96px;border-radius:50%;background:var(--blue-soft)}
.service h3{margin-top:16px;font-size:22px;font-weight:400;line-height:27px}
.slide-arrow{top:212px}
.service-detail{left:136px;top:459px;width:928px;height:354px;background:var(--white)}
.service-detail::before{content:"";position:absolute;left:438px;top:-26px;border:26px solid transparent;border-top:0;border-bottom-color:var(--white)}
.detail-photo{left:31px;top:34px;width:356px;height:286px;background:linear-gradient(120deg,#23415c,#7d8a96 50%,#3a2c24)}
.service-detail h3{left:428px;top:64px;font-size:29px;font-weight:400}
.service-detail p{left:428px;top:112px;width:465px;font-size:16px;line-height:26px;color:var(--text)}

/* insights */
.insights{height:660px}
.insights .section-title{top:78px}
.feature-card{left:111px;top:164px;width:482px;height:412px;background:linear-gradient(160deg,#2b4060,#4a5e7a 45%,#1d232b);color:var(--white)}
.feature-card .meta{left:38px;top:258px;font-size:17px}
.feature-card h3{left:38px;top:298px;width:420px;font-size:22px;line-height:27px;font-weight:700}
.post-card{left:615px;width:473px;height:194px;background:#f7f7f7}
.post-photo{left:0;top:0;width:193px;height:194px}
.post-card .meta{left:225px;top:36px;font-size:16px}
.post-card h3{left:225px;top:74px;width:230px;font-size:19px;line-height:23px;font-weight:700}
.meta svg{vertical-align:-2px;margin-right:6px}

/* testimonials */
.testimonials{height:532px;background:linear-gradient(90deg,#5a4a3e 0%,#9b8675 30%,#c7b8a8 55%,#c9a98a 80%,#8a7060 100%)}
.testimonials h2{left:113px;top:223px;font-size:42px;line-height:50px;font-weight:900;color:var(--white)}
.t-arrows{left:113px;top:327px;display:flex;gap:13px}
.quote-box{left:588px;top:63px;width:500px;height:406px;background:var(--blue);color:var(--white)}
.quote-mark{left:40px;top:38px}
.quote-box p{left:44px;top:88px;width:430px;font-style:italic;font-size:20px;line-height:31px;text-indent:60px}
.avatar{left:29px;top:263px;width:102px;height:102px;border-radius:50%;border:3px solid var(--white);background:linear-gradient(160deg,#d7b99a,#8a6e58)}
.author{left:156px;top:300px;font-size:22px;font-style:normal}

/* contact */
.contact{height:665px}
.contact .section-title{top:70px}
.contact-form{left:198px;top:162px;width:805px}
.field{position:absolute;border:1px solid #bbb;background:var(--white);font:15px 'Lato',sans-serif;color:#777;padding:14px 16px}
.submit{left:344px;top:371px;width:116px;height:57px;background:var(--blue);color:var(--white);font-weight:900;font-size:17px;display:flex;align-items:center;justify-content:center}

/* footer */
.site-footer{height:409px;background:var(--footer);color:#ddd}
.site-footer .brand{top:110px;color:var(--white)}
.footer-col{top:70px;font-size:16px}
.footer-col h4{font-size:17px;font-weight:700;color:var(--white);margin-bottom:20px}
.footer-col li{list-style:none;line-height:29px}
.contact-list li{display:flex;gap:8px;line-height:26px;margin-bottom:18px}
.contact-list svg{flex:none;margin-top:5px}
.footer-rule{left:111px;top:300px;width:978px;height:1px;background:#444}
.copyright{left:111px;top:343px;font-size:16px}
.socials{right:111px;top:327px;display:flex;gap:10px}
.socials span{width:51px;height:51px;border-radius:50%;border:2px solid var(--white)}
</style>
</head>
<body>

<header class="site-header">
  <a class="brand abs" href="#"><span class="brand-mark"></span>BRIGHT CORRIDOR</a>
  <div class="top-contact abs">
    <span><svg width="14" height="14" viewBox="0 0 24 24"><path fill="#149bd8" d="M6.6 10.8a15 15 0 0 0 6.6 6.6l2.2-2.2c.3-.3.7-.4 1-.2 1.1.4 2.3.6 3.6.6.6 0 1 .4 1 1V20c0 .6-.4 1-1 1A17 17 0 0 1 3 4c0-.6.4-1 1-1h3.5c.6 0 1 .4 1 1 0 1.3.2 2.5.6 3.6.1.3 0 .7-.2 1z"/></svg>1 555 014 2290</span>
    <span>|</span>
    <span><svg width="15" height="12" viewBox="0 0 24 18"><rect width="24" height="18" rx="2" fill="#149bd8"/><path d="M2 3l10 7 10-7" stroke="#fff" stroke-width="2" fill="none"/></svg>hello@brightcorridor.net</span>
  </div>
  <nav class="main-nav abs">
    <a class="active" href="#">Home</a><a href="#">About Us</a><a href="#">Services</a><a href="#">Insights</a><a href="#">Contact Us</a>
  </nav>
</header>

<section class="hero">
  <div class="hero-photo abs" role="img" aria-label="Smiling businesswoman working on a laptop in a bright office"></div>
  <h2 class="hero-title abs">BRIGHT CORRIDOR</h2>
  <p class="hero-sub abs">We are an IT business Company</p>
  <a class="hero-btn btn-outline abs" href="#">GET MORE INFO</a>
  <div class="hero-dots abs"><span></span><span></span><span></span></div>
</section>

<section class="welcome">
  <h1 class="abs">WELCOME TO<br>BRIGHT CORRIDOR</h1>
  <p class="abs">Nemo enim ipsam voluptatem quia voluptas sit aspe rnatur aut odit aut fugit, sed quia consequuntur agi i dolores es qui ratione voluptatem sequi nesciunque porro qi iqu am est, qui dolorem ipsum quia dolor it amet, consectet ur, adipisci velit, sed quia non numq uam eius modi tempora incid.</p>
  <a class="welcome-btn btn-outline abs" href="#">READ MORE</a>
  <div class="welcome-photo abs" role="img" aria-label="Colleagues reviewing charts on a laptop at a meeting table"></div>
  <div class="play abs"><svg width="22" height="24" viewBox="0 0 22 24"><path d="M2 1l19 11L2 23z" fill="#fff"/></svg></div>
  <div class="about-badge abs"><small>ABOUT</small>BRIGHT<br>CORRIDOR</div>
</section>

<section class="services">
  <h2 class="section-title abs">SERVICES</h2>
  <svg class="slide-arrow abs" style="left:56px" width="20" height="34" viewBox="0 0 20 34"><path d="M17 3L4 17l13 14" stroke="#666" stroke-width="3" fill="none"/></svg>
  <svg class="slide-arrow abs" style="left:1126px" width="20" height="34" viewBox="0 0 20 34"><path d="M3 3l13 14L3 31" stroke="#666" stroke-width="3" fill="none"/></svg>

  <div class="service abs" style="left:105px">
    <div class="service-ring"><div class="service-icon" role="img" aria-label="Business consulting illustration"></div></div>
    <h3>Business<br>Consulting</h3>
  </div>
  <div class="service abs" style="left:302px">
    <div class="service-ring"><div class="service-icon" role="img" aria-label="Data and analytics illustration"></div></div>
    <h3>Data and<br>Analytics</h3>
  </div>
  <div class="service current abs" style="left:500px">
    <div class="service-ring"><div class="service-icon" role="img" aria-label="IT outsourcing illustration"></div></div>
    <h3>IT<br>Outsourcing</h3>
  </div>
  <div class="service abs" style="left:698px">
    <div class="service-ring"><div class="service-icon" role="img" aria-label="Business process illustration"></div></div>
    <h3>Business<br>Process</h3>
  </div>
  <div class="service abs" style="left:896px">
    <div class="service-ring"><div class="service-icon" role="img" aria-label="Application services illustration"></div></div>
    <h3>Application<br>Services</h3>
  </div>

  <div class="service-detail abs">
    <div class="detail-photo abs" role="img" aria-label="Two colleagues pointing at a network of connected people icons"></div>
    <h3 class="abs">IT Outsourcing</h3>
    <p class="abs">Nam libero tempore, cum soluta nobis est eligendi optio cuie que nihil impedit quo minus id quod maxime placeat facere possimus, omnis voluptas assumenda est, omnis dolor repell endus. Temporibus autem quibusdam et aut officiis debitis aut rerum necessitatibus saepe eveniet ut et voluptates repu diandae sint et molestia taque.</p>
  </div>
</section>

<section class="insights">
  <h2 class="section-title abs">INSIGHTS</h2>
  <article class="feature-card abs" role="img" aria-label="Presenter pointing at charts on a large screen">
    <div class="meta abs"><svg width="15" height="15" viewBox="0 0 16 16"><rect x="1" y="3" width="14" height="12" fill="none" stroke="#fff" stroke-width="1.6"/><path d="M1 6h14M4 1v3M12 1v3" stroke="#fff" stroke-width="1.6"/></svg>26/04/2021</div>
    <h3 class="abs">Nam libero tempore, cum soluta nobis est eligendi optio cumque nihil impedi tuo minus id quod max</h3>
  </article>
  <article class="post-card abs" style="top:164px">
    <div class="post-photo abs" role="img" aria-label="Woman checking her phone at a desk with a laptop" style="background:linear-gradient(135deg,#c9c2b4,#6e6152 60%,#3c3a3a)"></div>
    <div class="meta abs"><svg width="15" height="15" viewBox="0 0 16 16"><rect x="1" y="3" width="14" height="12" fill="none" stroke="#149bd8" stroke-width="1.6"/><path d="M1 6h14M4 1v3M12 1v3" stroke="#149bd8" stroke-width="1.6"/></svg>26/04/2021</div>
    <h3 class="abs">Nam libero tempore, cum est eligendi optio cumque tuo minus id</h3>
  </article>
  <article class="post-card abs" style="top:382px">
    <div class="post-photo abs" role="img" aria-label="Team meeting in a glass-walled conference room" style="background:linear-gradient(135deg,#dfe6ea,#8a98a3 50%,#2f3338)"></div>
    <div class="meta abs"><svg width="15" height="15" viewBox="0 0 16 16"><rect x="1" y="3" width="14" height="12" fill="none" stroke="#149bd8" stroke-width="1.6"/><path d="M1 6h14M4 1v3M12 1v3" stroke="#149bd8" stroke-width="1.6"/></svg>26/04/2021</div>
    <h3 class="abs">Nam libero tempore, cum est eligendi optio cumque tuo minus id</h3>
  </article>
</section>

<section class="testimonials" role="img" aria-label="Smiling woman holding a phone and a folder">
  <h2 class="abs">CLIENT<br>TESTIMONIALS</h2>
  <div class="t-arrows abs">
    <svg width="26" height="26" viewBox="0 0 26 26"><circle cx="13" cy="13" r="13" fill="#fff"/><path d="M15 7l-6 6 6 6" stroke="#222" stroke-width="3" fill="none"/></svg>
    <svg width="26" height="26" viewBox="0 0 26 26"><circle cx="13" cy="13" r="13" fill="#fff"/><path d="M11 7l6 6-6 6" stroke="#222" stroke-width="3" fill="none"/></svg>
  </div>
  <blockquote class="quote-box abs">
    <svg class="quote-mark abs" width="56" height="50" viewBox="0 0 56 50"><path d="M4 48C0 30 6 10 24 2l2 6C16 14 14 24 16 30c6 0 10 4 10 9s-4 9-10 9zM34 48c-4-18 2-38 20-46l2 6c-10 6-12 16-10 22 6 0 10 4 10 9s-4 9-10 9z" fill="#fff"/></svg>
    <p class="abs">dignissiml os ducimus qui blanditiis praese ntium voluptamvi deleniti atque corrupti quos dol ores et quas molse stias excepturi sint occaecatis piditate non prtuo vent, similique sunt in culpa qui officia deserurnt mollitia.</p>
    <div class="avatar abs" role="img" aria-label="Client portrait"></div>
    <cite class="author abs">Mara Lindqvist</cite>
  </blockquote>
</section>

<section class="contact">
  <h2 class="section-title abs">CONTACT US</h2>
  <form class="contact-form abs">
    <div class="field" style="left:0;top:0;width:394px;height:50px">Name:</div>
    <div class="field" style="left:411px;top:0;width:394px;height:50px">Email:</div>
    <div class="field" style="left:0;top:71px;width:394px;height:50px">Phone No:</div>
    <div class="field" style="left:411px;top:71px;width:394px;height:50px">Address:</div>
    <div class="field" style="left:0;top:141px;width:805px;height:52px">Subject:</div>
    <div class="field" style="left:0;top:211px;width:805px;height:119px">Message:</div>
    <div class="submit abs">SUBMIT</div>
  </form>
</section>

<footer class="site-footer">
  <a class="brand abs" href="#"><span class="brand-mark"></span>BRIGHT CORRIDOR</a>
  <div class="footer-col abs" style="left:482px">
    <h4>QUICK LINKS</h4>
    <ul><li><a href="#">Legal information</a></li><li><a href="#">Data protection (GDPR)</a></li><li><a href="#">Website owner declaration</a></li></ul>
  </div>
  <div class="footer-col abs" style="left:765px">
    <h4>CONTACT US</h4>
    <ul class="contact-list">
      <li><svg width="12" height="16" viewBox="0 0 12 16"><path d="M6 0a6 6 0 0 0-6 6c0 4 6 10 6 10s6-6 6-10a6 6 0 0 0-6-6zm0 8.5A2.5 2.5 0 1 1 6 3.5a2.5 2.5 0 0 1 0 5z" fill="#149bd8"/></svg><span>Nam libero tempore, cum soluta<br>nobis est eligendi optio</span></li>
      <li><svg width="14" height="14" viewBox="0 0 24 24"><path fill="#149bd8" d="M6.6 10.8a15 15 0 0 0 6.6 6.6l2.2-2.2c.3-.3.7-.4 1-.2 1.1.4 2.3.6 3.6.6.6 0 1 .4 1 1V20c0 .6-.4 1-1 1A17 17 0 0 1 3 4c0-.6.4-1 1-1h3.5c.6 0 1 .4 1 1 0 1.3.2 2.5.6 3.6.1.3 0 .7-.2 1z"/></svg><span>1 555 014 2290</span></li>
      <li><svg width="15" height="12" viewBox="0 0 24 18"><rect width="24" height="18" rx="2" fill="#149bd8"/><path d="M2 3l10 7 10-7" stroke="#262626" stroke-width="2" fill="none"/></svg><span>hello@brightcorridor.net</span></li>
    </ul>
  </div>
  <div class="footer-rule abs"></div>
  <p class="copyright abs">Copyright © 2021, Bright Corridor. All rights reserved.</p>
  <div class="socials abs"><span aria-label="Social profile"></span><span aria-label="Social profile"></span><span aria-label="Social profile"></span></div>
</footer>

</body>
</html>
```